8 Page Cheerleading Brochure, promoting travel options

Creation of an 8 Page A4 Brochure, portrait layout and print ready. To promote Cheerleading travel options and services to cheer gyms.
Front page to feature cheer image
Pages to include destination images and hotel images.

Colors
e34197
ec1f27

```html
<!DOCTYPE html>
<html lang="en">
<head>
<meta charset="utf-8">
<title>Cheer Travel Brochure</title>
<link href="https://fonts.googleapis.com/css2?family=Open+Sans:wght@400;600;700;800&display=swap" rel="stylesheet">
<style>
:root{
  --red:#ec1f27;
  --deep-red:#a8101c;
  --pink:#e34197;
  --grey-bg:#d5d6d8;
  --row:#ececec;
  --row-alt:#f7f7f7;
  --ink:#333;
  --muted:#666;
  --white:#fff;
}
*{box-sizing:border-box;margin:0;padding:0}
html,body{width:1200px;height:3141px;overflow:hidden}
body{background:var(--grey-bg);font-family:"Open Sans",Arial,sans-serif;color:var(--ink);position:relative}
.spread{position:absolute;left:110px;width:980px;height:696px;display:flex;box-shadow:0 6px 18px rgba(0,0,0,.25)}
.page{position:relative;width:490px;height:696px;background:var(--white);overflow:hidden}
.photo{position:absolute}
.photo-city{background:linear-gradient(160deg,#7d93ad,#4d6078 55%,#8c7f62)}
.photo-cheer{background:linear-gradient(180deg,#2a2a2e,#7a1a22 45%,#1b1b22)}
.photo-texas{background:linear-gradient(180deg,#3b6fb0,#c79a5d 70%,#6e5a3f)}
.photo-nanjing{background:linear-gradient(180deg,#1a2a4a,#b05a2a 60%,#222)}
.photo-hawaii{background:linear-gradient(180deg,#6fb2e0,#2aa3b8 55%,#e6d4a8)}
.photo-orlando{background:linear-gradient(180deg,#4d8ad0,#2d6a3a 65%,#3a3a3a)}
.photo-beach{background:linear-gradient(160deg,#aee0f0,#3fa4c8 55%,#e7d8b4)}
.photo-hotel{background:linear-gradient(160deg,#9cc7e8,#506a88)}
.photo-pool{background:linear-gradient(160deg,#7fd0f0,#2e8fc0)}
.photo-palm{background:linear-gradient(160deg,#f2b56b,#5b7b46)}
.photo-temple{background:linear-gradient(160deg,#e0b080,#5a2a1a)}
.round{position:absolute;border-radius:50%;border:4px solid var(--white);box-shadow:0 0 0 2px var(--red)}
.curve{position:absolute;left:0;width:490px}
.contact-line{position:absolute;left:0;right:0;text-align:center;font-size:12px;color:var(--muted)}
.contact-line svg{vertical-align:-2px;margin:0 3px 0 6px}
.foot{position:absolute;left:0;right:0;bottom:12px;height:24px}
.foot-bar{position:absolute;left:0;top:0;height:24px;width:300px;background:var(--red);border-radius:0 14px 14px 0;color:var(--white);font-size:10.5px;font-weight:600;line-height:24px;padding-left:16px}
.brand{position:absolute;right:18px;top:2px;display:flex;align-items:center;gap:6px}
.brand-name{font-size:11px;font-weight:800;color:var(--red);line-height:10px;width:86px;text-align:right}
.brand-mark{width:16px;height:16px;background:#777}
.title-xl{font-weight:800;color:var(--red);letter-spacing:-.5px}
.h2{font-weight:800;color:var(--red);font-size:16px}
.body{font-size:10px;line-height:1.35}
.center{text-align:center}
.itin{position:absolute;left:18px;right:18px;border-collapse:collapse;font-size:7.5px}
.itin td{padding:0 8px;height:20px;border-bottom:2px solid var(--white)}
.itin tr:nth-child(odd) td{background:var(--row)}
.itin tr:nth-child(even) td{background:var(--row-alt)}
.itin td:first-child{width:62px}
.itin td:last-child{width:88px;border-left:2px solid var(--white)}
.itin-label{position:absolute;left:18px;font-size:7.5px;color:var(--muted)}
.pill{position:absolute;background:var(--pink);color:var(--white);font-weight:700;font-size:10.5px;border-radius:12px;padding:4px 14px}
.pill-right{right:14px}
.accom{position:absolute;left:18px;font-size:10px;line-height:1.35}
.book{position:absolute;width:80px;height:80px;border-radius:50%;background:var(--pink);border:4px solid var(--white);box-shadow:0 0 0 2px var(--pink);color:var(--white);font-weight:800;font-size:15px;line-height:17px;display:flex;align-items:center;justify-content:center;text-align:center}
.red-panel{position:absolute;left:0;top:0;width:490px;background:linear-gradient(180deg,var(--red),var(--deep-red))}
.on-red{color:var(--white)}
.ticks{list-style:none;font-size:10.5px;line-height:1.45}
.ticks li::before{content:"";display:inline-block;width:7px;height:7px;border-radius:50%;background:var(--pink);margin-right:8px}
.services{position:absolute;left:18px;right:18px;display:grid;grid-template-columns:repeat(6,1fr);row-gap:10px;font-size:6px;text-align:center;color:var(--muted)}
.service-icon{width:20px;height:20px;margin:0 auto 3px;border:1.5px solid #888;border-radius:50%}
</style>
</head>
<body>

<!-- Spread 1: covers -->
<section class="spread" style="top:84px">
  <div class="page">
    <div class="photo" style="left:0;top:0;width:490px;height:130px;background:linear-gradient(135deg,#3b3b3f,#1e1e22)"></div>
    <div class="photo photo-city" role="img" aria-label="City skyline with river and bridge" style="left:0;top:0;width:250px;height:520px;clip-path:polygon(0 0,100% 0,100% 100%,0 100%)"></div>
    <div class="photo" style="left:250px;top:0;width:240px;height:520px;background:linear-gradient(180deg,#2a2a2e,#4a4a50 60%,#ddd)"></div>
    <div class="title-xl" style="position:absolute;right:20px;top:38px;font-size:30px">CHEER TRAVEL</div>
    <div class="on-red" style="position:absolute;right:20px;top:78px;font-size:13.5px;font-weight:600">Cheer Nationals, Flights &amp; Accommodation</div>
    <div class="on-red body" style="position:absolute;right:20px;top:118px;width:220px;text-align:right">Dedicated Nationals Accommodation site, with live rates and booking functionality.<br><b>http://cheerstay.example.com/</b></div>
    <div class="on-red body" style="position:absolute;right:20px;top:178px">Customised packages for Larger Groups.</div>
    <svg class="curve" style="top:430px" height="120" viewBox="0 0 490 120" preserveAspectRatio="none" aria-hidden="true">
      <path d="M0 70 Q250 120 490 20 L490 40 Q250 140 0 95Z" fill="var(--red)"/>
      <path d="M0 95 Q250 140 490 40 L490 120 L0 120Z" fill="#f4f4f4"/>
    </svg>
    <div class="round photo-beach" role="img" aria-label="Aerial beach and coastline" style="left:20px;top:490px;width:120px;height:120px"></div>
    <div class="contact-line" style="top:616px">For more information please contact us <svg width="12" height="12" viewBox="0 0 24 24"><path d="M6.6 10.8a15 15 0 0 0 6.6 6.6l2.2-2.2a1 1 0 0 1 1-.25 11 11 0 0 0 3.6.6 1 1 0 0 1 1 1V20a1 1 0 0 1-1 1A17 17 0 0 1 3 4a1 1 0 0 1 1-1h3.5a1 1 0 0 1 1 1 11 11 0 0 0 .6 3.6 1 1 0 0 1-.25 1Z" fill="#555"/></svg>(02) 9000 4815</div>
    <div class="foot"><div class="foot-bar">www.meridian.travel | enquiry@meridian.travel</div><div class="brand"><span class="brand-name">MERIDIAN GROUP TRAVEL</span><span class="brand-mark"></span></div></div>
  </div>
  <div class="page">
    <div class="photo photo-cheer" role="img" aria-label="Cheerleading team in red and black uniforms" style="left:0;top:0;width:490px;height:520px"></div>
    <svg class="curve" style="top:420px" height="130" viewBox="0 0 490 130" preserveAspectRatio="none" aria-hidden="true">
      <path d="M0 40 Q200 130 490 60 L490 80 Q200 150 0 62Z" fill="var(--red)"/>
      <path d="M0 62 Q200 150 490 80 L490 130 L0 130Z" fill="var(--white)"/>
    </svg>
    <div class="book" style="left:385px;top:425px">BOOK<br>NOW</div>
    <div class="title-xl" style="position:absolute;left:0;right:0;top:530px;text-align:center;font-size:44px">CHEER TRAVEL</div>
    <div class="contact-line" style="top:616px">For more information please contact us <svg width="12" height="12" viewBox="0 0 24 24"><path d="M6.6 10.8a15 15 0 0 0 6.6 6.6l2.2-2.2a1 1 0 0 1 1-.25 11 11 0 0 0 3.6.6 1 1 0 0 1 1 1V20a1 1 0 0 1-1 1A17 17 0 0 1 3 4a1 1 0 0 1 1-1h3.5a1 1 0 0 1 1 1 11 11 0 0 0 .6 3.6 1 1 0 0 1-.25 1Z" fill="#555"/></svg>(02) 9000 4815</div>
    <div class="foot"><div class="foot-bar">www.meridian.travel | enquiry@meridian.travel</div><div class="brand"><span class="brand-name">MERIDIAN GROUP TRAVEL</span><span class="brand-mark"></span></div></div>
  </div>
</section>

<!-- Spread 2: about us + desert -->
<section class="spread" style="top:833px">
  <div class="page">
    <div class="red-panel" style="height:330px"></div>
    <svg class="curve" style="top:300px" height="60" viewBox="0 0 490 60" preserveAspectRatio="none" aria-hidden="true"><path d="M0 30 Q250 70 490 0 L490 60 L0 60Z" fill="var(--white)"/></svg>
    <div class="h2 on-red" style="position:absolute;left:18px;top:26px;font-size:20px">ABOUT US</div>
    <div class="body on-red" style="position:absolute;left:18px;top:58px;width:450px">
      <p>Meridian Group Travel was established in 2001, originally specialising in Basketball Tours and quickly expanding to provide a variety of other sports options including cheerleading. Our customers have enjoyed destinations including the USA, Canada, China, Singapore, Vietnam, Europe, UK, South Africa, New Zealand and Australia.</p>
      <p style="margin-top:10px">Meridian are the official Travel Partner of the Southern Cross All Star Cheer Federation.</p>
      <p style="margin-top:10px">Our understanding of the unique requirements of group travel and our personalised approach makes us the ideal choice in planning, sourcing and managing the perfect tour for your school or club. Our ever-growing global network allows us to offer exclusive experiences that are inaccessible to others. Our dedicated Tour Coordinators thoroughly consult with coaches and coaches to tailor an itinerary and tour management plan that meets each unique set of requirements.</p>
    </div>
    <div style="position:absolute;left:18px;top:360px;font-size:10.5px">We can assist in providing:</div>
    <ul class="ticks" style="position:absolute;left:18px;top:378px;width:450px">
      <li>Customised Itineraries</li><li>Group Payment Plans</li><li>Trusted, Quality Suppliers</li><li>Negotiated Group Discounts on airfares, accommodation, transport and activities</li>
    </ul>
    <div class="body" style="position:absolute;left:18px;top:460px;width:450px">Meridian's passion and mission remains to provide 'once in a lifetime' experiences to all of our valued customers.</div>
    <div style="position:absolute;left:18px;top:496px;font-size:10px;font-weight:700;color:var(--red)">Services</div>
    <div class="services" style="top:516px">
      <div><div class="service-icon"></div>Custom packages to your needs</div>
      <div><div class="service-icon"></div>Face to face client meetings</div>
      <div><div class="service-icon"></div>Hosted information evenings</div>
      <div><div class="service-icon"></div>Regular tour updates</div>
      <div><div class="service-icon"></div>Tour leader pack with full itinerary</div>
      <div></div>
      <div><div class="service-icon"></div>Risk assessment templates</div>
      <div><div class="service-icon"></div>Tour kit partner offers</div>
      <div><div class="service-icon"></div>Around the clock assistance</div>
    </div>
    <div class="foot"><div class="foot-bar">www.meridian.travel | enquiry@meridian.travel</div><div class="brand"><span class="brand-name">MERIDIAN GROUP TRAVEL</span><span class="brand-mark"></span></div></div>
  </div>
  <div class="page">
    <div class="red-panel" style="height:300px"></div>
    <svg class="curve" style="top:270px" height="60" viewBox="0 0 490 60" preserveAspectRatio="none" aria-hidden="true"><path d="M0 0 Q250 70 490 30 L490 60 L0 60Z" fill="var(--white)"/></svg>
    <div class="round photo-palm" role="img" aria-label="Desert resort at sunset" style="left:14px;top:18px;width:62px;height:62px"></div>
    <div class="round photo-hotel" role="img" aria-label="Palm-lined hotel exterior" style="left:14px;top:96px;width:62px;height:62px"></div>
    <div class="round photo-pool" role="img" aria-label="Hotel swimming pool" style="left:14px;top:174px;width:62px;height:62px"></div>
    <div class="on-red" style="position:absolute;left:92px;top:22px;font-size:13.5px;font-weight:700">Desert Showdown. Palm Springs, California</div>
    <div class="body on-red" style="position:absolute;left:92px;top:46px;width:380px">Desert Showdown is one of the largest Cheer events in the US, run by Spirit Events Co and is renowned for the production quality. The event is held at the Palm Springs Convention centre and draws in some of the West Coast's most talented teams. You'll see some familiar names like Coastal All Stars, Force Cheer, Pacific Spark, as well as many other West Coast programs</div>
    <div class="pill" style="left:92px;top:140px;background:var(--white);color:var(--red)">Packages from $3,300</div>
    <div class="accom on-red" style="left:92px;top:172px"><b>Featured accommodation</b><br>• Anaheim Garden Inn<br>• Cathedral City Express Inn<br>• Palm Fairway Golf Resort</div>
    <div class="itin-label" style="top:320px">Sample Itinerary</div>
    <table class="itin" style="top:336px">
      <tr><td>Day 1</td><td>Depart Australia. On arrival transfer to your hotel where you will have the chance to take in the Walk of Fame.</td><td>Los Angeles</td></tr>
      <tr><td>Day 2</td><td>Spend the day at the theme park, enjoying rides, characters and shows.</td><td>Los Angeles</td></tr>
      <tr><td>Day 3</td><td>Fine tune your routine with a morning training session before transferring out to Palm Springs</td><td>Palm Springs</td></tr>
      <tr><td>Day 4</td><td>Competition Day 1</td><td>Palm Springs</td></tr>
      <tr><td>Day 5</td><td>Competition Day 2</td><td>Palm Springs</td></tr>
      <tr><td>Day 6</td><td>Ride the Aerial Tramway up the cliffs of the canyon, taking in the spectacular views.</td><td>Palm Springs</td></tr>
      <tr><td>Day 7</td><td>Transfer back to Los Angeles, spending some time at the pier before your evening flight home.</td><td>Los Angeles</td></tr>
      <tr><td>Day 8</td><td>In transit</td><td>In transit</td></tr>
      <tr><td>Day 9</td><td>Arrive home</td><td></td></tr>
    </table>
    <div class="foot"><div class="foot-bar">www.meridian.travel | enquiry@meridian.travel</div><div class="brand"><span class="brand-name">MERIDIAN GROUP TRAVEL</span><span class="brand-mark"></span></div></div>
  </div>
</section>

<!-- Spread 3: Texas + Nanjing -->
<section class="spread" style="top:1591px">
  <div class="page">
    <div class="photo photo-texas" role="img" aria-label="Large resort hotel in Texas at dusk" style="left:0;top:0;width:490px;height:170px"></div>
    <svg class="curve" style="top:120px" height="70" viewBox="0 0 490 70" preserveAspectRatio="none" aria-hidden="true">
      <path d="M0 50 Q250 10 490 30 L490 42 Q250 24 0 62Z" fill="var(--red)"/>
      <path d="M0 62 Q250 24 490 42 L490 70 L0 70Z" fill="var(--white)"/>
    </svg>
    <div class="round photo-pool" role="img" aria-label="Resort indoor atrium" style="left:26px;top:108px;width:70px;height:70px"></div>
    <div class="round photo-palm" role="img" aria-label="Texas welcome sign" style="left:106px;top:100px;width:70px;height:70px"></div>
    <div class="h2 center" style="position:absolute;left:0;right:0;top:196px;font-size:14px">Lone Star All-Star Nationals. Grapevine, Texas</div>
    <div class="body center" style="position:absolute;left:30px;right:30px;top:220px">The event is open to Pom, Hip Hop, Jazz, Lyrical/Contemporary, Kick and Variety. The event takes place at the Grapevine Lakeside Resort which sprawls across 400,000 square feet.</div>
    <div class="body center" style="position:absolute;left:0;right:0;top:252px">Featured accommodation<br>• Addison Park Inn &nbsp;&nbsp;• Grapevine Lakeside Resort</div>
    <table class="itin" style="top:296px">
      <tr><td>Day 1</td><td>Depart Australia. On arrival transfer to your hotel</td><td>Dallas</td></tr>
      <tr><td>Day 2</td><td>Morning training session to fine tune your routine. Check out nearby Fort Worth for a taste of Texas life.</td><td>Dallas</td></tr>
      <tr><td>Day 3</td><td>Fine tune your routine with a training session. Afternoon at leisure to explore Dallas</td><td>Dallas</td></tr>
      <tr><td>Day 4</td><td>Competition Day 1</td><td>Dallas</td></tr>
      <tr><td>Day 5</td><td>Competition Day 2</td><td>Dallas</td></tr>
      <tr><td>Day 6</td><td>Competition Day 3</td><td>Dallas</td></tr>
      <tr><td>Day 7</td><td>Head to Lakeview Outlet Centre for some bargain hunting before boarding your evening flight home</td><td>Dallas</td></tr>
      <tr><td>Day 8</td><td>In transit</td><td>Dallas</td></tr>
      <tr><td>Day 9</td><td>Arrive home</td><td></td></tr>
    </table>
    <div class="pill pill-right" style="top:628px">Packages from $2,900</div>
    <div class="foot"><div class="foot-bar">www.meridian.travel | enquiry@meridian.travel</div><div class="brand"><span class="brand-name">MERIDIAN GROUP TRAVEL</span><span class="brand-mark"></span></div></div>
  </div>
  <div class="page">
    <div class="photo photo-nanjing" role="img" aria-label="Illuminated riverside old town in Nanjing at night" style="left:0;top:0;width:490px;height:170px"></div>
    <svg class="curve" style="top:120px" height="70" viewBox="0 0 490 70" preserveAspectRatio="none" aria-hidden="true">
      <path d="M0 30 Q250 24 490 0 L490 14 Q250 40 0 44Z" fill="var(--red)"/>
      <path d="M0 44 Q250 40 490 14 L490 70 L0 70Z" fill="var(--white)"/>
    </svg>
    <div class="h2 center" style="position:absolute;left:0;right:0;top:196px;font-size:12.5px;line-height:1.3">ALL-CHINA CHEER LEAGUE OPEN<br>CHEER &amp; DANCE CHAMPIONSHIP. NANJING, CHINA</div>
    <div class="body center" style="position:absolute;left:40px;right:40px;top:234px">Join teams from across all regions of China, as well as surrounding countries for China's largest cheer event. Hosted in the former Imperial capital of Nanjing, you will have the chance to explore the city, interact with other competitors and visit other parts of China.</div>
    <div class="round photo-hotel" role="img" aria-label="Modern hotel tower" style="left:115px;top:300px;width:62px;height:62px"></div>
    <div class="round photo-temple" role="img" aria-label="Traditional pagoda" style="left:214px;top:300px;width:62px;height:62px"></div>
    <div class="round photo-city" role="img" aria-label="Nanjing city skyline" style="left:313px;top:300px;width:62px;height:62px"></div>
    <table class="itin" style="top:386px">
      <tr><td>Day 1</td><td>Depart Australia. Teams arrive and register with event staff. Teams warm-up.</td><td>Nanjing</td></tr>
      <tr><td>Day 2</td><td>Teams warm-up, VIP reception, first section of competitions</td><td>Nanjing</td></tr>
      <tr><td>Day 3</td><td>Opening ceremony, second and third section of competitions</td><td>Nanjing</td></tr>
      <tr><td>Day 4</td><td>Nanjing city tour</td><td>Nanjing</td></tr>
      <tr><td>Day 5</td><td>Depart for Beijing, Shanghai or Xian to explore China.</td><td>Nanjing</td></tr>
    </table>
    <div class="accom" style="top:500px">Featured accommodation<br>• Nanjing Riverside Hotel &nbsp;• Nanjing Central Hotel</div>
    <div class="pill pill-right" style="top:628px">Packages from $2,950</div>
    <div class="foot"><div class="foot-bar">www.meridian.travel | enquiry@meridian.travel</div><div class="brand"><span class="brand-name">MERIDIAN GROUP TRAVEL</span><span class="brand-mark"></span></div></div>
  </div>
</section>

<!-- Spread 4: Hawaii + Worlds -->
<section class="spread" style="top:2345px">
  <div class="page">
    <div class="photo photo-hawaii" role="img" aria-label="Waikiki beach with hotels and crater headland" style="left:0;top:0;width:490px;height:240px"></div>
    <svg class="curve" style="top:180px" height="80" viewBox="0 0 490 80" preserveAspectRatio="none" aria-hidden="true">
      <path d="M0 40 Q250 80 490 20 L490 34 Q250 96 0 54Z" fill="var(--red)"/>
      <path d="M0 54 Q250 96 490 34 L490 80 L0 80Z" fill="var(--white)"/>
    </svg>
    <div class="h2" style="position:absolute;left:18px;top:248px;font-size:17px">HAWAII</div>
    <div class="body" style="position:absolute;left:18px;top:270px;width:450px">Soak up the sun, surf and sand of Hawaii as well as competing against strong US Gyms in one of a couple of events open to Australian groups. You will also have the chance to see some of the sights of the Oahu and soak in some of the Hawaiian culture.</div>
    <table class="itin" style="top:330px">
      <tr><td>Day 1</td><td>Depart Australia. On arrival transfer to your hotel.</td><td>Honolulu</td></tr>
      <tr><td>Day 2</td><td>Visit Pearl Harbour and the USS Arizona Memorial. Hike up to Diamond Head Crater, taking in the view of the city.</td><td>Honolulu</td></tr>
      <tr><td>Day 3</td><td>Fine tune your routine with a training session. Afternoon at leisure</td><td>Honolulu</td></tr>
      <tr><td>Day 4</td><td>Competition Day 1</td><td>Honolulu</td></tr>
      <tr><td>Day 5</td><td>Competition Day 2</td><td>Honolulu</td></tr>
      <tr><td>Day 6</td><td>Visit Splash Water Park</td><td>Honolulu</td></tr>
      <tr><td>Day 7</td><td>Depart for Australia</td><td>Honolulu</td></tr>
      <tr><td>Day 8</td><td>In transit</td><td>In transit</td></tr>
    </table>
    <div class="pill pill-right" style="top:606px">Packages from $2,800</div>
    <div class="accom" style="top:628px">Featured accommodation<br>• Waikiki Lagoon Village • Waikiki Breeze Hotel • Waikiki Plaza Suites</div>
    <div class="foot"><div class="foot-bar">www.meridian.travel | enquiry@meridian.travel</div><div class="brand"><span class="brand-name">MERIDIAN GROUP TRAVEL</span><span class="brand-mark"></span></div></div>
  </div>
  <div class="page">
    <div class="photo photo-orlando" role="img" aria-label="Sports complex entrance with globe sculpture" style="left:0;top:0;width:490px;height:240px"></div>
    <svg class="curve" style="top:180px" height="80" viewBox="0 0 490 80" preserveAspectRatio="none" aria-hidden="true">
      <path d="M0 20 Q250 90 490 36 L490 50 Q250 104 0 34Z" fill="var(--red)"/>
      <path d="M0 34 Q250 104 490 50 L490 80 L0 80Z" fill="var(--white)"/>
    </svg>
    <div class="h2" style="position:absolute;left:18px;top:248px;font-size:17px">WORLDS</div>
    <div class="body" style="position:absolute;left:18px;top:270px;width:450px">The peak of the Sport! Hosted at the Grand Sports Complex, located at the Lakeside Theme Resort Orlando. Enjoy mixing and competing against teams from all over the world. You will also have the chance to enjoy the thrills and rides of the theme parks.</div>
    <table class="itin" style="top:318px">
      <tr><td>Day 1</td><td>Depart Australia. On arrival transfer to your Orlando hotel</td><td>Orlando</td></tr>
      <tr><td>Day 2</td><td>Morning Training Session. Afternoon visit to outlets.</td><td>Orlando</td></tr>
      <tr><td>Day 3</td><td>Day at leisure to explore Orlando</td><td>Orlando</td></tr>
      <tr><td>Day 4</td><td>Worlds Day 1</td><td>Orlando</td></tr>
      <tr><td>Day 5</td><td>Worlds Day 2</td><td>Orlando</td></tr>
      <tr><td>Day 6</td><td>Worlds Day 3</td><td>Orlando</td></tr>
      <tr><td>Day 7</td><td>Spend the day enjoying the parks</td><td>Orlando</td></tr>
      <tr><td>Day 8</td><td>Depart for Australia</td><td>Orlando</td></tr>
      <tr><td>Day 9</td><td>In transit</td><td>In transit</td></tr>
      <tr><td>Day 10</td><td>Arrive home</td><td>In transit</td></tr>
    </table>
    <div class="pill pill-right" style="top:606px">Packages from $3,400</div>
    <div class="accom" style="top:628px">Featured accommodation<br>• Allstar Sports Lodge • Melody Resort</div>
    <div class="foot"><div class="foot-bar">www.meridian.travel | enquiry@meridian.travel</div><div class="brand"><span class="brand-name">MERIDIAN GROUP TRAVEL</span><span class="brand-mark"></span></div></div>
  </div>
</section>

</body>
</html>
```